I need a new business card design for my pharmacy.

I need a business card design. I will include my logo.
The card needs to be readable. I prefer to have my logo on one side along with my website, the other side includes the other information. Please use combination of black, neon green, white, and silver. This needs to catch the eye but yet be clearly visible and legible. Thanks

Industry/Entity Type

Pharmacy

Contact Information for Business Card

It needs to have the following information listed:
Mel's Apothecary Owner/Pharm D.
7134 North Brook Lane
Sioux Falls, SD 57231
Phone 605-318-6207
Fax 605-318-6209
email: mel@melsapothecary-example.com
www.melsapothecary-example.com
Store hours Monday-Friday 8 am- 7 pm
Saturday 8 am- 12 pm
Sunday Closed
Please utilize the colors black, white, and neon green, maybe silver.

Requirements
Must have
• It needs to be easily readable!
Nice to have
• It should catch the eye.
Should not have
• Do not use any other colors except listed: black, neon green, white, & silver.

```html
<!DOCTYPE html>
<html lang="en">
<head>
<meta charset="utf-8">
<title>Mel's Apothecary — Business Card</title>
<link rel="stylesheet" href="https://fonts.googleapis.com/css2?family=Open+Sans:wght@400;600;700&display=swap">
<style>
  :root {
    --ink: #0b0b0b;
    --ink-soft: #1c1c1c;
    --neon: #8cc63f;
    --white: #ffffff;
    --silver: #c9ccd1;
    --stage: #e6e7e9;
  }
  * { box-sizing: border-box; margin: 0; padding: 0; }
  html, body { width: 1200px; height: 913px; overflow: hidden; }
  body {
    background: var(--stage);
    font-family: "Open Sans", Arial, sans-serif;
    position: relative;
  }
  .card {
    position: absolute;
    width: 525px;
    height: 300px;
    border-radius: 16px;
    overflow: hidden;
    background: linear-gradient(160deg, var(--ink-soft) 0%, var(--ink) 55%);
    color: var(--white);
    box-shadow: 0 10px 28px rgba(0,0,0,.25);
  }
  .card--front { left: 60px; top: 130px; }
  .card--back { left: 615px; top: 470px; }

  /* front */
  .brand {
    position: absolute; left: 28px; top: 52px;
    display: flex; align-items: center; gap: 14px;
  }
  .brand__dot { width: 14px; height: 14px; border-radius: 50%; background: var(--neon); }
  .brand__divider { width: 1px; height: 44px; background: var(--silver); opacity: .7; }
  .brand__name { font-size: 22px; font-weight: 700; letter-spacing: -.3px; }

  .identity {
    position: absolute; right: 24px; top: 22px; text-align: right;
  }
  .identity__name { font-size: 20px; font-weight: 700; line-height: 1.1; }
  .identity__role { font-size: 12px; font-weight: 600; color: var(--neon); }
  .identity__tab {
    position: absolute; right: -24px; top: 0; width: 8px; height: 26px;
    background: var(--white);
  }
  .rule--short {
    position: absolute; right: 24px; top: 76px; width: 220px; height: 1px;
    background: var(--silver); opacity: .6;
  }
  .hours {
    position: absolute; right: 24px; top: 84px; text-align: right;
    font-size: 12.5px; line-height: 1.45;
  }
  .hours__line, .contact__line { display: flex; justify-content: flex-end; align-items: center; gap: 6px; }
  .icon { width: 12px; height: 12px; flex: none; }
  .contact {
    position: absolute; right: 24px; top: 132px; text-align: right;
    font-size: 12.5px; line-height: 1.45;
  }
  .rule--long {
    position: absolute; left: 0; top: 214px; width: 100%; height: 1px;
    background: linear-gradient(90deg, var(--silver), rgba(201,204,209,.15));
    opacity: .7;
  }
  .address {
    position: absolute; left: 28px; top: 226px;
    font-size: 13px; line-height: 1.35;
  }
  .band {
    position: absolute; bottom: 0; height: 26px;
  }
  .band--white-left { left: 0; width: 160px; background: var(--white); }
  .band--neon { left: 160px; right: 0; background: var(--neon); }

  /* back */
  .mark {
    position: absolute; left: 0; right: 0; top: 88px;
    display: flex; justify-content: center; align-items: center; gap: 14px;
  }
  .mark__dot { width: 22px; height: 22px; border-radius: 50%; background: var(--neon); }
  .mark__name { font-size: 36px; font-weight: 700; letter-spacing: -.5px; }
  .footer-band {
    position: absolute; left: 0; right: 0; bottom: 0; height: 40px;
    display: flex;
  }
  .footer-band__end { width: 70px; background: var(--white); }
  .footer-band__main {
    flex: 1; background: var(--neon); color: var(--ink);
    display: flex; align-items: center; justify-content: center;
    font-size: 13px; font-weight: 600;
  }
</style>
</head>
<body>

<section class="card card--front" aria-label="Business card front">
  <div class="brand">
    <span class="brand__dot"></span>
    <span class="brand__divider"></span>
    <span class="brand__name">Mel's Apothecary</span>
  </div>

  <div class="identity">
    <span class="identity__tab"></span>
    <div class="identity__name">Mel's Apothecary</div>
    <div class="identity__role">Owner/Pharm D</div>
  </div>
  <div class="rule--short"></div>

  <div class="hours">
    <div class="hours__line">Store hours Monday-Friday 8 am - 7 pm
      <svg class="icon" viewBox="0 0 12 12"><path d="M1.5 6.5 4.5 9.5 10.5 2.5" fill="none" stroke="#8cc63f" stroke-width="2"/></svg>
    </div>
    <div class="hours__line">Saturdays 8 am - 12 pm, Sundays closed
      <svg class="icon" viewBox="0 0 12 12"><path d="M1.5 6.5 4.5 9.5 10.5 2.5" fill="none" stroke="#8cc63f" stroke-width="2"/></svg>
    </div>
  </div>

  <div class="contact">
    <div class="contact__line">605-318-6207
      <svg class="icon" viewBox="0 0 12 12"><path d="M2.5 1h2.2l1 2.6-1.3 1a6 6 0 0 0 3 3l1-1.3 2.6 1v2.2A1.5 1.5 0 0 1 9.5 11 8.5 8.5 0 0 1 1 2.5 1.5 1.5 0 0 1 2.5 1z" fill="#8cc63f"/></svg>
    </div>
    <div class="contact__line">605-318-6209
      <svg class="icon" viewBox="0 0 12 12"><rect x="3" y="1" width="6" height="3" fill="#8cc63f"/><rect x="1" y="4.5" width="10" height="4.5" rx="1" fill="#8cc63f"/><rect x="3" y="8" width="6" height="3" fill="#8cc63f"/></svg>
    </div>
    <div class="contact__line">mel@melsapothecary-example.com
      <svg class="icon" viewBox="0 0 12 12"><rect x="1" y="2.5" width="10" height="7" fill="none" stroke="#8cc63f" stroke-width="1.2"/><path d="M1 2.5 6 6.5 11 2.5" fill="none" stroke="#8cc63f" stroke-width="1.2"/></svg>
    </div>
  </div>

  <div class="rule--long"></div>

  <address class="address" style="font-style:normal">
    7134 North Brook Lane<br>
    Sioux Falls, SD 57231
  </address>

  <div class="band band--white-left"></div>
  <div class="band band--neon"></div>
</section>

<section class="card card--back" aria-label="Business card back">
  <div class="mark">
    <span class="mark__dot"></span>
    <span class="mark__name">Mel's Apothecary</span>
  </div>
  <div class="footer-band">
    <span class="footer-band__end"></span>
    <span class="footer-band__main">www.melsapothecary-example.com</span>
    <span class="footer-band__end"></span>
  </div>
</section>

</body>
</html>
```